Morvex Business Card (intended for Business Card sized magnet)

Hi guys,

I would like to get a design for my business card for the restaurant. The design must be single sided as I intend to produce business card sized magnets.

The File attached must me on and I'm open for new ides

Can you please ensure that the design meets Cardowell's magnetic business card size specifications:

http://www.cardowell.example.au/custom-magnets.aspx?txi=15695&xnid=TopNav_Magnetic+Business+Cards+(linked+item)_Magnets_Marketing+Products&xnav=TopNav

Full Bleed Size (starting document size):
90 x 52 mm
1062 x 615 pixels
* Finished artwork should use the full bleed dimensions for best results.

Document Trim Size (final size after being cut):
87 x 49 mm
1028 x 579 pixels
* Please be sure to keep all text within the safe margin.

Resolution:
300 DPI

The winning design/source files need to meet these specifications.

Thanks
Updates

Hi guys, can I see more options please Thanks

```html
<!DOCTYPE html>
<html lang="en">
<head>
<meta charset="utf-8">
<title>Morvex Business Card</title>
<link rel="stylesheet" href="https://fonts.googleapis.com/css2?family=Tinos&family=Questrial&display=swap">
<style>
  :root {
    --page-bg: #e4e5e7;
    --card-bg: #ffffff;
    --card-shade: #ececec;
    --teal: #1aa6b7;
    --ink: #111111;
    --accent-red: #9e1b2e;
    --icon-red: #c52a30;
    --muted: #8a8a8a;
    --band-light: #e9e9e9;
    --band-mid: #cfcfcf;
  }
  * { margin: 0; padding: 0; box-sizing: border-box; }
  html, body { width: 1200px; height: 900px; overflow: hidden; }
  body {
    background: var(--page-bg);
    display: flex;
    align-items: center;
    justify-content: center;
  }
  .card {
    position: relative;
    width: 1000px;
    height: 563px;
    background: linear-gradient(180deg, var(--card-bg) 0%, var(--card-shade) 100%);
    box-shadow: 0 8px 24px rgba(0,0,0,0.18);
    overflow: hidden;
  }
  .card-edges { position: absolute; inset: 0; }
  .brand-name {
    position: absolute;
    right: 56px;
    top: 34px;
    font-family: "Tinos", "Times New Roman", serif;
    font-size: 96px;
    color: var(--ink);
    line-height: 1;
    letter-spacing: 1px;
  }
  .pattern-band {
    position: absolute;
    left: 0;
    top: 150px;
    width: 100%;
    height: 110px;
    border-top: 2px solid var(--ink);
    border-bottom: 2px solid var(--ink);
    padding: 8px 0;
  }
  .pattern-fill {
    height: 100%;
    background: linear-gradient(90deg, var(--band-light), var(--band-mid), var(--band-light));
    border-top: 1px solid var(--ink);
    border-bottom: 1px solid var(--ink);
  }
  .holder {
    position: absolute;
    right: 56px;
    top: 284px;
    text-align: right;
    font-family: "Questrial", "Century Gothic", sans-serif;
  }
  .holder-name { color: var(--accent-red); font-size: 44px; letter-spacing: 1px; line-height: 1; }
  .holder-role { color: var(--muted); font-size: 20px; margin-top: 4px; }
  .contact-list {
    position: absolute;
    left: 52px;
    top: 330px;
    list-style: none;
    font-family: "Questrial", "Century Gothic", sans-serif;
    font-size: 22px;
    color: var(--ink);
  }
  .contact-list li { display: flex; align-items: center; gap: 20px; height: 44px; }
  .contact-icon { width: 28px; height: 28px; flex: none; }
</style>
</head>
<body>

  <section class="card" aria-label="Business card">
    <svg class="card-edges" width="1000" height="563" viewBox="0 0 1000 563" aria-hidden="true">
      <path d="M90,0 C130,16 160,20 200,20 H1000 V0 Z" fill="var(--teal)"/>
      <path d="M0,563 V548 H800 C880,548 910,520 1000,516 V563 Z" fill="var(--teal)"/>
    </svg>

    <div class="brand-name">Morvex</div>

    <div class="pattern-band">
      <div class="pattern-fill" role="img" aria-label="Black geometric star-and-knot border pattern with small teal, yellow and red dots"></div>
    </div>

    <div class="holder">
      <div class="holder-name">YOUR NAME</div>
      <div class="holder-role">Designation</div>
    </div>

    <ul class="contact-list">
      <li>
        <svg class="contact-icon" viewBox="0 0 20 20" aria-hidden="true"><rect x="5" y="1.5" width="10" height="17" rx="2" fill="none" stroke="var(--icon-red)" stroke-width="1.6"/><circle cx="10" cy="15.5" r="0.9" fill="var(--icon-red)"/></svg>
        <span>+000 (50) 555-01-98</span>
      </li>
      <li>
        <svg class="contact-icon" viewBox="0 0 20 20" aria-hidden="true"><circle cx="10" cy="10" r="8.5" fill="none" stroke="var(--icon-red)" stroke-width="1.8"/><path d="M6,6 Q9,8 8,11 Q11,12 10,15 M12,5 Q14,8 15,9" fill="none" stroke="var(--icon-red)" stroke-width="1.8"/></svg>
        <span>www.morvexdine.example</span>
      </li>
      <li>
        <svg class="contact-icon" viewBox="0 0 20 20" aria-hidden="true"><rect x="1.5" y="4" width="17" height="12" fill="var(--icon-red)"/><path d="M1.5,4 L10,11 L18.5,4" fill="none" stroke="#fff" stroke-width="1.4"/></svg>
        <span>info@morvexdine.example</span>
      </li>
      <li>
        <svg class="contact-icon" viewBox="0 0 20 20" aria-hidden="true"><path d="M10,19 C6,13 4,10 4,7.5 A6,6 0 0 1 16,7.5 C16,10 14,13 10,19 Z" fill="var(--icon-red)"/><circle cx="10" cy="7.5" r="2.3" fill="#fff"/></svg>
        <span>Harbor City, Sample Region</span>
      </li>
    </ul>
  </section>

</body>
</html>
```